Build PowerPoint for New Logo & Letterhead

I have started my own consulting firm and created a logo and letterhead (attached) am looking PowerPoint template. My name is Dorrit Okonkwo-Haverly and the company is called Birchpoint Consulting. We primarily use PowerPoint files to display analyses, maps and key talking points from interviews and/or recommendations. We use the documents more to facilitate discussion with our target audiences. Most of the time our PowerPoint document is printed as handouts for our clients and not projected.

Target Market(s)

Healthcare provider organizations (hospitals, health systems, physician groups)

Industry/Entity Type

Healthcare

Font styles to use
Sans Serif

Colors
abd036
1f9ad1
0355a3

Requirements
Must have
• I would like to cover page to play off of the letterhead in some fashion. I want the design to provide plenty of space for text, graphics, maps, pictures, etc.
• We will usually include our clients logo somewhere on the document. Historically it is prominent on the cover page and then in one of the corners on all of the pages thereafter.

```html
<!DOCTYPE html>
<html lang="en">
<head>
<meta charset="utf-8">
<title>Birchpoint Consulting – PowerPoint Template Overview</title>
<link href="https://fonts.googleapis.com/css2?family=Open+Sans:wght@400;600;700&display=swap" rel="stylesheet">
<style>
:root{
  --green:#abd036;
  --blue:#1f9ad1;
  --navy:#0355a3;
  --grey:#8c8c8c;
  --ink:#333;
  --text:#666;
  --page:#e9e9e9;
  --rule:#e2e2e2;
}
*{box-sizing:border-box;margin:0;padding:0}
html,body{width:906px;height:1200px;overflow:hidden;background:var(--page);font-family:"Open Sans",Arial,sans-serif}
.sheet{position:relative;width:906px;height:1200px}
.slide{position:absolute;width:285px;height:160px;background:#fff;overflow:hidden;box-shadow:0 1px 3px rgba(0,0,0,.18)}
.c1{left:15px}.c2{left:311px}.c3{left:606px}
.r1{top:18px}.r2{top:186px}.r3{top:354px}.r4{top:523px}.r5{top:691px}.r6{top:859px}.r7{top:1027px}
.ttl{position:absolute;left:15px;top:13px;font-size:11px;font-weight:600;color:var(--ink);letter-spacing:.1px}
.sub{font-size:5px;font-weight:700;color:var(--blue);margin-bottom:2px}
.txt{font-size:4px;line-height:5px;color:var(--text)}
.txt li{margin-left:6px;margin-bottom:2px}
.txt li.in{margin-left:12px;list-style:"– "}
.foot{position:absolute;left:0;right:0;bottom:0;height:12px}
.foot .line{position:absolute;left:0;right:0;top:0;height:1.5px;background:linear-gradient(90deg,var(--green) 0 38%,var(--blue) 38% 100%)}
.foot .mark{position:absolute;left:12px;top:3px;font-size:4.5px;font-weight:700;color:var(--navy)}
.foot .copy{position:absolute;left:0;right:0;top:4px;text-align:center;font-size:3px;color:#999}
.foot .num{position:absolute;right:10px;top:4px;font-size:3px;color:#999}
.brand{font-weight:700;color:var(--navy);font-size:7px;letter-spacing:.3px}
.brand.white{color:#fff}
.photo{position:absolute}
.cols{position:absolute;top:40px;display:flex;gap:8px}
/* cover */
.cover{background:linear-gradient(135deg,#2aa6dc,#1f8fcb 60%,#1c84c3)}
.cover .people{position:absolute;inset:0;background:linear-gradient(180deg,rgba(255,255,255,.08),rgba(255,255,255,0) 60%)}
.cover .lead{position:absolute;left:40px;right:40px;top:56px;text-align:center;color:#fff;font-size:5.5px;line-height:7px}
.cover .copyr{position:absolute;left:0;right:0;top:78px;text-align:center;color:#e6f4fb;font-size:3.5px}
.cover .brand{position:absolute;left:0;right:0;top:110px;text-align:center}
/* title slides */
.ptitle{position:absolute;left:8px;font-weight:700;font-size:10.5px;color:var(--navy)}
.psub{position:absolute;left:8px;font-size:5.5px;color:#333}
.pdate{position:absolute;left:8px;font-size:3.8px;color:#555}
/* toc */
.toc{position:absolute;left:15px;top:38px;display:grid;grid-template-columns:repeat(3,82px);row-gap:10px;column-gap:6px}
.toc .head{display:flex;align-items:center;gap:4px;font-size:4.5px;font-weight:600;color:#333}
.toc .n{width:13px;height:13px;border:1.2px solid var(--green);border-radius:50%;display:flex;align-items:center;justify-content:center;font-size:5px;color:var(--navy)}
.toc p{font-size:3.6px;line-height:4.5px;color:var(--text);margin-top:2px;width:66px}
/* team */
.team{position:absolute;left:22px;top:35px;display:grid;grid-template-columns:repeat(3,84px);row-gap:5px}
.member{text-align:center;width:36px}
.member .face{width:24px;height:24px;border-radius:50%;margin:0 auto;background:radial-gradient(circle at 50% 40%,#e8eef3,#b9cbd8);border:1.5px solid #dfe6ea}
.member b{display:block;font-size:4.2px;color:var(--blue);font-style:italic;margin-top:1px}
.member span{display:block;font-size:3.2px;color:#888}
/* table */
.tbl{position:absolute;left:15px;top:36px;width:256px;border-collapse:collapse;font-size:3.3px;color:var(--text)}
.tbl th{color:#fff;font-size:4px;font-weight:700;height:11px;text-align:center}
.tbl td{padding:2px 3px;vertical-align:top;height:14px;line-height:4px}
.tbl tr:nth-child(odd) td{background:#f1f1f1}
/* chevrons */
.chev-txt{position:absolute;top:80px;font-size:3.6px;line-height:4.6px;color:var(--text);width:60px}
/* dark slides */
.dark{background:#222}
.overlay-title{position:absolute;left:15px;top:13px;font-size:10.5px;font-weight:600;color:#fff}
.icons{position:absolute;left:0;right:0;bottom:12px;height:45px;background:#fff;display:flex;justify-content:space-around;padding:0 10px}
.icon-item{text-align:center;width:58px;margin-top:-10px}
.icon-item .ic{width:17px;height:17px;border-radius:50%;margin:0 auto;display:flex;align-items:center;justify-content:center;border:2px solid #fff}
.icon-item b{display:block;font-size:4.2px;color:var(--green);margin-top:2px}
.icon-item p{font-size:3.3px;line-height:4px;color:var(--text)}
</style>
</head>
<body>
<main class="sheet">

<!-- 1 Cover -->
<section class="slide c1 r1 cover">
  <div class="people" role="img" aria-label="Faded photograph of medical staff walking in a bright hospital corridor"></div>
  <p class="lead"><b>Lorem ipsum</b> dolor sit amet, consectetur adipiscing elit. Suspendisse eget ligula mollis, mattis libero eget, rutrum ipsum.</p>
  <p class="copyr">Copyright © 2016 Birchpoint Consulting All rights reserved.</p>
  <div class="brand white">Birchpoint</div>
</section>

<!-- 2 Title light -->
<section class="slide c2 r1">
  <div class="photo" style="left:0;top:0;width:285px;height:118px;background:linear-gradient(120deg,#d9d3cc,#b9a99a 45%,#e7e2dc)" role="img" aria-label="Photograph of a smiling nurse with a stethoscope talking to a patient"></div>
  <svg class="photo" style="left:0;top:96px" width="285" height="64" viewBox="0 0 285 64">
    <polygon points="0,12 150,12 175,0 285,0 285,64 0,64" fill="#fff"/>
    <polygon points="0,10 150,10 175,-2 285,-2 285,0 176,0 151,13 0,13" fill="#0355a3"/>
    <polygon points="0,13 151,13 0,16" fill="#abd036"/>
    <polygon points="0,13 151,13 151,15 0,17" fill="#abd036"/>
  </svg>
  <div class="ptitle" style="top:120px">Presentation Title</div>
  <div class="psub" style="top:134px">Subheading Presentation Title</div>
  <div class="pdate" style="top:146px">May 2016</div>
  <div class="brand" style="position:absolute;right:10px;top:138px">Birchpoint</div>
</section>

<!-- 3 Title dark -->
<section class="slide c3 r1 dark">
  <div class="photo" style="inset:0;background:linear-gradient(90deg,#1a1a1a 0 40%,#6a5d55 70%,#9c8c80)" role="img" aria-label="Darkened photograph of a nurse speaking with a patient"></div>
  <div class="ptitle" style="top:42px;color:#fff;font-size:12px">Presentation Title</div>
  <div class="psub" style="top:60px;color:#eee">Subheading Presentation Title</div>
  <div class="pdate" style="top:78px;color:#ccc">May 2016</div>
  <svg class="photo" style="left:0;top:124px" width="285" height="36" viewBox="0 0 285 36">
    <rect width="285" height="36" fill="#fff"/>
    <rect width="285" height="3" fill="#1f9ad1"/>
    <rect y="3" width="285" height="1.5" fill="#abd036"/>
  </svg>
  <div class="brand" style="position:absolute;left:12px;top:138px">Birchpoint</div>
  <div style="position:absolute;left:62px;top:135px;font-size:3.6px;line-height:8px;color:var(--blue)">dorrit@birchpointconsulting.co<br>Telephone 555.014.2288</div>
</section>

<!-- 4 Section slide -->
<section class="slide c1 r2">
  <div class="photo" style="left:0;top:0;width:285px;height:120px;background:linear-gradient(100deg,#cfe0ea,#eef3f6 45%,#f4ece3)" role="img" aria-label="Photograph of a smiling doctor with a stethoscope"></div>
  <svg class="photo" style="left:0;top:100px" width="285" height="60" viewBox="0 0 285 60">
    <polygon points="0,20 200,20 230,5 285,5 285,60 0,60" fill="#fff"/>
    <polygon points="0,18 200,18 230,3 285,3 285,5 230,5 200,20 0,20" fill="#1f9ad1"/>
  </svg>
  <div class="brand" style="position:absolute;right:12px;top:118px">Birchpoint</div>
  <div class="ptitle" style="top:138px;font-size:8.5px">Section Slide</div>
  <div class="psub" style="top:151px;font-size:5px">Divider Presentation Title</div>
  <div style="position:absolute;left:0;right:0;bottom:0;height:2px;background:var(--green)"></div>
</section>

<!-- 5 Table of content -->
<section class="slide c2 r2">
  <h2 class="ttl">Table of Content</h2>
  <div class="toc">
    <div><div class="head"><span class="n">1</span>Lorem Ipsum</div><p>Lorem ipsum dolor sit amet, te ullum corpora delicata duo. Rebum insolens pri eu.</p></div>
    <div><div class="head"><span class="n">2</span>Lorem Ipsum</div><p>Lorem ipsum dolor sit amet, te ullum corpora delicata duo. Rebum insolens pri eu.</p></div>
    <div><div class="head"><span class="n">3</span>Lorem Ipsum</div><p>Lorem ipsum dolor sit amet, te ullum corpora delicata duo. Rebum insolens pri eu.</p></div>
    <div><div class="head"><span class="n">4</span>Lorem Ipsum</div><p>Lorem ipsum dolor sit amet, te ullum corpora delicata duo. Rebum insolens pri eu.</p></div>
    <div><div class="head"><span class="n">5</span>Lorem Ipsum</div><p>Lorem ipsum dolor sit amet, te ullum corpora delicata duo. Rebum insolens pri eu.</p></div>
    <div><div class="head"><span class="n">6</span>Lorem Ipsum</div><p>Lorem ipsum dolor sit amet, te ullum corpora delicata duo. Rebum insolens pri eu.</p></div>
  </div>
  <footer class="foot"><span class="line"></span><span class="mark">Birchpoint</span><span class="copy">Copyright © 2016 Birchpoint Consulting All rights reserved.</span><span class="num">5</span></footer>
</section>

<!-- 6 One column -->
<section class="slide c3 r2">
  <h2 class="ttl">One Column</h2>
  <div style="position:absolute;left:15px;top:38px;width:255px">
    <p class="sub">Lorem Ipsum</p>
    <ul class="txt">
      <li>Lorem ipsum dolor sit amet, te ullum corpora delicata duo. Rebum insolens pri eu. No alia tota modus qui.</li>
      <li class="in">Sint brute at usu. Duo iisque appareat adversarium at.</li>
      <li>Lorem ipsum dolor sit amet, te ullum corpora delicata duo. Rebum insolens pri eu. No alia tota modus qui.</li>
      <li class="in">Sint brute at usu. Duo iisque appareat adversarium at.</li>
      <li>Lorem ipsum dolor sit amet, te ullum corpora delicata duo. Rebum insolens pri eu. No alia tota modus qui.</li>
      <li class="in">Sint brute at usu. Duo iisque appareat adversarium at.</li>
      <li>Lorem ipsum dolor sit amet, te ullum corpora delicata duo. Rebum insolens pri eu. No alia tota modus qui.</li>
      <li class="in">Sint brute at usu. Duo iisque appareat adversarium at.</li>
    </ul>
  </div>
  <footer class="foot"><span class="line"></span><span class="mark">Birchpoint</span><span class="copy">Copyright © 2016 Birchpoint Consulting All rights reserved.</span><span class="num">6</span></footer>
</section>

<!-- 7 Two column -->
<section class="slide c1 r3">
  <h2 class="ttl">Two Column</h2>
  <div class="cols" style="left:15px">
    <div style="width:122px">
      <p class="sub">Lorem Ipsum</p>
      <ul class="txt">
        <li>Lorem ipsum dolor sit amet, te ullum corpora delicata duo. Rebum insolens pri eu. No alia tota modus qui.</li>
        <li class="in">Sint brute at usu. Duo iisque appareat adversarium at.</li>
        <li>Lorem ipsum dolor sit amet, te ullum corpora delicata duo. Rebum insolens pri eu. No alia tota modus qui.</li>
        <li class="in">Sint brute at usu. Duo iisque appareat adversarium at.</li>
        <li>Lorem ipsum dolor sit amet, te ullum corpora delicata duo. Rebum insolens pri eu.</li>
      </ul>
    </div>
    <div style="width:122px;border-left:1px dotted #ccc;padding-left:6px">
      <p class="sub">Lorem Ipsum</p>
      <ul class="txt">
        <li>Lorem ipsum dolor sit amet, te ullum corpora delicata duo. Rebum insolens pri eu. No alia tota modus qui.</li>
        <li class="in">Sint brute at usu. Duo iisque appareat adversarium at.</li>
        <li>Lorem ipsum dolor sit amet, te ullum corpora delicata duo. Rebum insolens pri eu. No alia tota modus qui.</li>
        <li class="in">Sint brute at usu. Duo iisque appareat adversarium at.</li>
        <li>Lorem ipsum dolor sit amet, te ullum corpora delicata duo. Rebum insolens pri eu.</li>
      </ul>
    </div>
  </div>
  <footer class="foot"><span class="line"></span><span class="mark">Birchpoint</span><span class="copy">Copyright © 2016 Birchpoint Consulting All rights reserved.</span><span class="num">7</span></footer>
</section>

<!-- 8 Left column -->
<section class="slide c2 r3">
  <h2 class="ttl">Left Column</h2>
  <div style="position:absolute;left:15px;top:40px;width:122px">
    <p class="sub">Lorem Ipsum</p>
    <ul class="txt">
      <li>Lorem ipsum dolor sit amet, te ullum corpora delicata duo. Rebum insolens pri eu. No alia tota modus qui.</li>
      <li class="in">Sint brute at usu. Duo iisque appareat adversarium at.</li>
      <li>Lorem ipsum dolor sit amet, te ullum corpora delicata duo. Rebum insolens pri eu. No alia tota modus qui.</li>
      <li class="in">Sint brute at usu. Duo iisque appareat adversarium at.</li>
      <li>Lorem ipsum dolor sit amet, te ullum corpora delicata duo. Rebum insolens pri eu.</li>
    </ul>
  </div>
  <svg style="position:absolute;left:150px;top:38px" width="120" height="105" viewBox="0 0 120 105">
    <polygon points="60,2 71,22 49,22" fill="#d9d9d9"/>
    <polygon points="47,25 73,25 85,47 35,47" fill="#0355a3"/>
    <polygon points="33,50 87,50 99,72 21,72" fill="#1f9ad1"/>
    <polygon points="19,75 101,75 114,98 6,98" fill="#abd036"/>
  </svg>
  <footer class="foot"><span class="line"></span><span class="mark">Birchpoint</span><span class="copy">Copyright © 2016 Birchpoint Consulting All rights reserved.</span><span class="num">8</span></footer>
</section>

<!-- 9 Right column with image -->
<section class="slide c3 r3">
  <div class="photo" style="left:0;top:0;width:135px;height:148px;background:linear-gradient(180deg,#f2f5f7,#dfe7ec)" role="img" aria-label="Photograph of a smiling male doctor in a white coat with a stethoscope"></div>
  <h2 class="ttl" style="left:148px;font-size:9px">Right Column With Image</h2>
  <div style="position:absolute;left:150px;top:38px;width:122px">
    <p class="sub" style="color:var(--green)">Lorem Ipsum</p>
    <ul class="txt">
      <li>Lorem ipsum dolor sit amet, te ullum corpora delicata duo. Rebum insolens pri eu. No alia tota modus qui.</li>
      <li class="in">Sint brute at usu. Duo iisque appareat adversarium at.</li>
      <li>Lorem ipsum dolor sit amet, te ullum corpora delicata duo. Rebum insolens pri eu. No alia tota modus qui.</li>
      <li class="in">Sint brute at usu. Duo iisque appareat adversarium at.</li>
      <li>Lorem ipsum dolor sit amet, te ullum corpora delicata duo. Rebum insolens pri eu.</li>
    </ul>
  </div>
  <footer class="foot"><span class="line"></span><span class="mark">Birchpoint</span><span class="copy">Copyright © 2016 Birchpoint Consulting All rights reserved.</span><span class="num">9</span></footer>
</section>

<!-- 10 Our team -->
<section class="slide c1 r4">
  <h2 class="ttl">Our Team</h2>
  <div class="team">
    <div class="member"><div class="face" role="img" aria-label="Team member portrait"></div><b>John Doe</b><span>Doctor</span></div>
    <div class="member"><div class="face" role="img" aria-label="Team member portrait"></div><b>John Doe</b><span>Doctor</span></div>
    <div class="member"><div class="face" role="img" aria-label="Team member portrait"></div><b>John Doe</b><span>Doctor</span></div>
    <div class="member"><div class="face" role="img" aria-label="Team member portrait"></div><b>John Doe</b><span>Doctor</span></div>
    <div class="member"><div class="face" role="img" aria-label="Team member portrait"></div><b>John Doe</b><span>Doctor</span></div>
    <div class="member"><div class="face" role="img" aria-label="Team member portrait"></div><b>John Doe</b><span>Doctor</span></div>
  </div>
  <footer class="foot"><span class="line"></span><span class="mark">Birchpoint</span><span class="copy">Copyright © 2016 Birchpoint Consulting All rights reserved.</span><span class="num">10</span></footer>
</section>

<!-- 11 Table sample -->
<section class="slide c2 r4">
  <h2 class="ttl">Table Sample</h2>
  <table class="tbl">
    <thead><tr>
      <th style="background:var(--green)">Lorem ipsum</th>
      <th style="background:var(--blue)">Lorem ipsum 1</th>
      <th style="background:var(--navy)">Lorem ipsum 2</th>
      <th style="background:var(--grey)">Lorem ipsum 3</th>
    </tr></thead>
    <tbody>
      <tr><td>Lorem ipsum dolor sit amet, consectetur adipiscing elit.</td><td>Lorem ipsum dolor sit amet, consectetur elit.</td><td>Lorem ipsum dolor sit amet, consectetur elit.</td><td>Quisque vel sem luctus, finibus leo.</td></tr>
      <tr><td>Lorem ipsum dolor sit amet, consectetur adipiscing elit.</td><td>Lorem ipsum dolor sit amet, consectetur elit.</td><td>Quisque vel sem luctus, finibus leo.</td><td>Lorem ipsum dolor sit amet, consectetur elit.</td></tr>
      <tr><td>Lorem ipsum dolor sit amet, consectetur adipiscing elit.</td><td>Lorem ipsum dolor sit amet, consectetur elit.</td><td>Lorem ipsum dolor sit amet, consectetur elit.</td><td>Lorem ipsum dolor sit amet, consectetur elit.</td></tr>
      <tr><td>Lorem ipsum dolor sit amet.</td><td>Lorem ipsum dolor sit amet.</td><td>Lorem ipsum dolor sit amet.</td><td>Lorem ipsum dolor sit amet.</td></tr>
    </tbody>
  </table>
  <footer class="foot"><span class="line"></span><span class="mark">Birchpoint</span><span class="copy">Copyright © 2016 Birchpoint Consulting All rights reserved.</span><span class="num">11</span></footer>
</section>

<!-- 12 About us -->
<section class="slide c3 r4">
  <h2 class="ttl">About Us</h2>
  <div class="photo" style="left:14px;top:44px;width:88px;height:88px;border-radius:50%;background:radial-gradient(circle at 50% 40%,#f4f7f9,#d3dee6)" role="img" aria-label="Circular photograph of a smiling male doctor"></div>
  <div style="position:absolute;left:112px;top:40px;width:160px">
    <p class="sub" style="font-style:italic">Lorem Ipsum is simply dummy</p>
    <p class="txt">Text of the printing and typesetting industry. Lorem Ipsum has been the industry's standard dummy text ever since the 1500s, when an unknown printer took a galley of type and scrambled it to make a type specimen book. It has survived not only five centuries, but also the leap into electronic typesetting, remaining essentially unchanged. It was popularised in the 1960s with the release of sheets containing Lorem Ipsum passages, and more recently with desktop publishing software. Lorem Ipsum has been the industry's standard dummy text ever since the 1500s, when an unknown printer took a galley of type and scrambled.</p>
  </div>
  <footer class="foot"><span class="line"></span><span class="mark">Birchpoint</span><span class="copy">Copyright © 2016 Birchpoint Consulting All rights reserved.</span><span class="num">12</span></footer>
</section>

<!-- 13 Pie chart -->
<section class="slide c1 r5">
  <h2 class="ttl">Pie Chart Sample</h2>
  <p style="position:absolute;left:0;right:0;top:38px;text-align:center;font-size:6px;font-weight:600;color:#444">Lorem ipsum dolar sit amet</p>
  <svg style="position:absolute;left:102px;top:50px" width="82" height="82" viewBox="0 0 82 82">
    <g transform="rotate(-90 41 41)">
      <circle cx="41" cy="41" r="19" fill="none" stroke="#abd036" stroke-width="38" pathLength="100" stroke-dasharray="58 100"/>
      <circle cx="41" cy="41" r="19" fill="none" stroke="#1f9ad1" stroke-width="38" pathLength="100" stroke-dasharray="23 100" stroke-dashoffset="-58"/>
      <circle cx="41" cy="41" r="19" fill="none" stroke="#0355a3" stroke-width="38" pathLength="100" stroke-dasharray="10 100" stroke-dashoffset="-81"/>
      <circle cx="41" cy="41" r="19" fill="none" stroke="#e0e0e0" stroke-width="38" pathLength="100" stroke-dasharray="9 100" stroke-dashoffset="-91"/>
    </g>
    <g font-size="5" fill="#fff" font-family="Open Sans, sans-serif">
      <text x="60" y="47">58%</text><text x="10" y="54">23%</text><text x="9" y="33">10%</text><text x="28" y="12" fill="#999">9%</text>
    </g>
  </svg>
  <div style="position:absolute;left:0;right:0;top:138px;display:flex;justify-content:center;gap:10px;font-size:3.4px;color:#777">
    <span><b style="color:var(--green)">■</b> Lorem ipsum</span><span><b style="color:var(--blue)">■</b> Lorem ipsum</span><span><b style="color:var(--navy)">■</b> Lorem ipsum</span><span><b style="color:#ccc">■</b> Lorem ipsum</span>
  </div>
  <footer class="foot"><span class="line"></span><span class="mark">Birchpoint</span><span class="copy">Copyright © 2016 Birchpoint Consulting All rights reserved.</span><span class="num">13</span></footer>
</section>

<!-- 14 Timeline -->
<section class="slide c2 r5">
  <h2 class="ttl">Timeline Sample</h2>
  <svg style="position:absolute;left:0;top:0" width="285" height="160" viewBox="0 0 285 160">
    <line x1="28" y1="92" x2="262" y2="92" stroke="#ccc" stroke-width="1"/>
    <g font-size="3.6" fill="#fff" text-anchor="middle" font-family="Open Sans, sans-serif">
      <rect x="34" y="40" width="40" height="34" fill="#abd036"/><line x1="54" y1="74" x2="54" y2="88" stroke="#ccc"/><circle cx="54" cy="88" r="1.5" fill="#abd036"/>
      <text x="54" y="48">Lorem ipsum</text><text x="54" y="53">dolor sit amet,</text><text x="54" y="58">consectetur</text><text x="54" y="63">adipiscing elit.</text>
      <rect x="93" y="40" width="40" height="34" fill="#1f9ad1"/><line x1="113" y1="74" x2="113" y2="88" stroke="#ccc"/><circle cx="113" cy="88" r="1.5" fill="#1f9ad1"/>
      <text x="113" y="48">Lorem ipsum</text><text x="113" y="53">dolor sit amet,</text><text x="113" y="58">consectetur</text><text x="113" y="63">adipiscing elit.</text>
      <rect x="152" y="40" width="40" height="34" fill="#0355a3"/><line x1="172" y1="74" x2="172" y2="88" stroke="#ccc"/><circle cx="172" cy="88" r="1.5" fill="#0355a3"/>
      <text x="172" y="48">Lorem ipsum</text><text x="172" y="53">dolor sit amet,</text><text x="172" y="58">consectetur</text><text x="172" y="63">adipiscing elit.</text>
      <rect x="211" y="40" width="40" height="34" fill="#8c8c8c"/><line x1="231" y1="74" x2="231" y2="88" stroke="#ccc"/><circle cx="231" cy="88" r="1.5" fill="#8c8c8c"/>
      <text x="231" y="48">Lorem ipsum</text><text x="231" y="53">dolor sit amet,</text><text x="231" y="58">consectetur</text><text x="231" y="63">adipiscing elit.</text>
      <line x1="83" y1="96" x2="83" y2="108" stroke="#ccc"/><circle cx="83" cy="96" r="1.5" fill="#8c8c8c"/><rect x="63" y="108" width="40" height="32" fill="#8c8c8c"/>
      <text x="83" y="116">Lorem ipsum</text><text x="83" y="121">dolor sit amet,</text><text x="83" y="126">consectetur</text><text x="83" y="131">adipiscing elit.</text>
      <line x1="142" y1="96" x2="142" y2="108" stroke="#ccc"/><circle cx="142" cy="96" r="1.5" fill="#0355a3"/><rect x="122" y="108" width="40" height="32" fill="#0355a3"/>
      <text x="142" y="116">Lorem ipsum</text><text x="142" y="121">dolor sit amet,</text><text x="142" y="126">consectetur</text><text x="142" y="131">adipiscing elit.</text>
      <line x1="201" y1="96" x2="201" y2="108" stroke="#ccc"/><circle cx="201" cy="96" r="1.5" fill="#1f9ad1"/><rect x="181" y="108" width="40" height="32" fill="#1f9ad1"/>
      <text x="201" y="116">Lorem ipsum</text><text x="201" y="121">dolor sit amet,</text><text x="201" y="126">consectetur</text><text x="201" y="131">adipiscing elit.</text>
    </g>
  </svg>
  <footer class="foot"><span class="line"></span><span class="mark">Birchpoint</span><span class="copy">Copyright © 2016 Birchpoint Consulting All rights reserved.</span><span class="num">14</span></footer>
</section>

<!-- 15 Chevron process -->
<section class="slide c3 r5">
  <h2 class="ttl">Basic Chevron Process</h2>
  <svg style="position:absolute;left:0;top:0" width="285" height="80" viewBox="0 0 285 80">
    <polygon points="20,38 96,38 106,54 96,70 20,70" fill="#abd036"/>
    <polygon points="100,38 176,38 186,54 176,70 100,70 110,54" fill="#1f9ad1"/>
    <polygon points="180,38 256,38 266,54 256,70 180,70 190,54" fill="#0355a3"/>
    <g font-size="6" fill="#fff" text-anchor="middle" font-family="Open Sans, sans-serif">
      <text x="60" y="56">Lorem ipsum</text><text x="144" y="56">Lorem ipsum</text><text x="224" y="56">Lorem ipsum</text>
    </g>
  </svg>
  <ul class="chev-txt" style="left:24px"><li>Lorem ipsum dolor sit amet, consectetur adipiscing elit.</li><li>Nunc quis dui dolor.</li><li>Maecenas sem nibh, congue a urna non, volutpat porttitor justo.</li></ul>
  <ul class="chev-txt" style="left:108px"><li>Lorem ipsum dolor sit amet, consectetur adipiscing elit.</li><li>Nunc quis dui dolor.</li><li>Maecenas sem nibh, congue a urna non, volutpat porttitor justo.</li></ul>
  <ul class="chev-txt" style="left:190px"><li>Lorem ipsum dolor sit amet, consectetur adipiscing elit.</li><li>Nunc quis dui dolor.</li><li>Maecenas sem nibh, congue a urna non, volutpat porttitor justo.</li></ul>
  <footer class="foot"><span class="line"></span><span class="mark">Birchpoint</span><span class="copy">Copyright © 2016 Birchpoint Consulting All rights reserved.</span><span class="num">15</span></footer>
</section>

<!-- 16 Venn -->
<section class="slide c1 r6">
  <h2 class="ttl">Linier VEEN</h2>
  <svg style="position:absolute;left:0;top:0" width="285" height="160" viewBox="0 0 285 160">
    <circle cx="70" cy="90" r="39" fill="#abd036" opacity=".92"/>
    <circle cx="142" cy="90" r="39" fill="#1f9ad1" opacity=".85"/>
    <circle cx="214" cy="90" r="39" fill="#0355a3" opacity=".82"/>
    <g font-size="3.8" fill="#fff" text-anchor="middle" font-family="Open Sans, sans-serif">
      <text x="70" y="74">Lorem ipsum dolor sit</text><text x="70" y="79">amet, consectetur</text><text x="70" y="84">adipiscing elit. Nunc</text><text x="70" y="89">quis dui dolor.</text><text x="70" y="94">Maecenas sem nibh,</text><text x="70" y="99">congue a urna non,</text><text x="70" y="104">volutpat porttitor</text><text x="70" y="109">justo.</text>
      <text x="142" y="74">Lorem ipsum dolor sit</text><text x="142" y="79">amet, consectetur</text><text x="142" y="84">adipiscing elit. Nunc</text><text x="142" y="89">quis dui dolor.</text><text x="142" y="94">Maecenas sem nibh,</text><text x="142" y="99">congue a urna non,</text><text x="142" y="104">volutpat porttitor</text><text x="142" y="109">justo.</text>
      <text x="214" y="74">Lorem ipsum dolor sit</text><text x="214" y="79">amet, consectetur</text><text x="214" y="84">adipiscing elit. Nunc</text><text x="214" y="89">quis dui dolor.</text><text x="214" y="94">Maecenas sem nibh,</text><text x="214" y="99">congue a urna non,</text><text x="214" y="104">volutpat porttitor</text><text x="214" y="109">justo.</text>
    </g>
  </svg>
  <footer class="foot"><span class="line"></span><span class="mark">Birchpoint</span><span class="copy">Copyright © 2016 Birchpoint Consulting All rights reserved.</span><span class="num">16</span></footer>
</section>

<!-- 17 Bar chart -->
<section class="slide c2 r6">
  <h2 class="ttl">Bar Chart Sample</h2>
  <p style="position:absolute;left:0;right:0;top:38px;text-align:center;font-size:6px;font-weight:600;color:#444">Lorem ipsum dolor sit amet</p>
  <svg style="position:absolute;left:0;top:0" width="285" height="160" viewBox="0 0 285 160">
    <g stroke="#eee" stroke-width=".5">
      <line x1="32" y1="54" x2="270" y2="54"/><line x1="32" y1="66" x2="270" y2="66"/><line x1="32" y1="78" x2="270" y2="78"/><line x1="32" y1="90" x2="270" y2="90"/><line x1="32" y1="102" x2="270" y2="102"/><line x1="32" y1="114" x2="270" y2="114"/>
    </g>
    <line x1="32" y1="126" x2="270" y2="126" stroke="#bbb" stroke-width=".6"/>
    <g font-size="3.5" fill="#888" text-anchor="end" font-family="Open Sans, sans-serif">
      <text x="28" y="56">6</text><text x="28" y="68">5</text><text x="28" y="80">4</text><text x="28" y="92">3</text><text x="28" y="104">2</text><text x="28" y="116">1</text><text x="28" y="128">0</text>
    </g>
    <rect x="40" y="76" width="8" height="50" fill="#abd036"/>
    <rect x="63" y="96" width="8" height="30" fill="#abd036"/>
    <rect x="86" y="84" width="8" height="42" fill="#abd036"/>
    <rect x="109" y="71" width="8" height="55" fill="#1f9ad1"/>
    <rect x="132" y="96" width="8" height="30" fill="#1f9ad1"/>
    <rect x="155" y="109" width="8" height="17" fill="#1f9ad1"/>
    <rect x="178" y="59" width="8" height="67" fill="#0355a3"/>
    <rect x="201" y="90" width="8" height="36" fill="#0355a3"/>
    <rect x="224" y="102" width="8" height="24" fill="#0355a3"/>
    <rect x="247" y="76" width="8" height="50" fill="#8c8c8c"/>
    <g font-size="3" fill="#888" text-anchor="middle" font-family="Open Sans, sans-serif">
      <text x="44" y="132">Category 1</text><text x="67" y="132">Category 2</text><text x="90" y="132">Category 3</text><text x="113" y="132">Category 4</text><text x="136" y="132">Category 5</text><text x="159" y="132">Category 6</text><text x="182" y="132">Category 7</text><text x="205" y="132">Category 8</text><text x="228" y="132">Category 9</text><text x="251" y="132">Category 10</text>
    </g>
  </svg>
  <footer class="foot"><span class="line"></span><span class="mark">Birchpoint</span><span class="copy">Copyright © 2016 Birchpoint Consulting All rights reserved.</span><span class="num">17</span></footer>
</section>

<!-- 18 Graphic sample -->
<section class="slide c3 r6">
  <h2 class="ttl">Graphic Sample</h2>
  <svg style="position:absolute;left:0;top:0" width="285" height="160" viewBox="0 0 285 160">
    <circle cx="142" cy="92" r="29" fill="none" stroke="#abd036" stroke-width="1.5"/>
    <g fill="#fff" stroke="#abd036" stroke-width="1.5">
      <circle cx="142" cy="63" r="8"/><circle cx="167" cy="78" r="8"/><circle cx="167" cy="107" r="8"/>
      <circle cx="142" cy="121" r="8"/><circle cx="117" cy="107" r="8"/><circle cx="117" cy="78" r="8"/>
    </g>
    <g fill="none" stroke="#abd036" stroke-width="1">
      <rect x="138" y="59" width="8" height="8"/>
      <circle cx="167" cy="78" r="3.5"/>
      <path d="M163 109 l3 -4 l2 2 l3 -4"/>
      <rect x="139.5" y="117" width="5" height="8" rx="1"/>
      <circle cx="117" cy="107" r="3.5"/><line x1="113.5" y1="107" x2="120.5" y2="107"/>
      <rect x="113" y="75" width="8" height="5"/><line x1="117" y1="80" x2="117" y2="82"/>
    </g>
    <text x="142" y="94" font-size="5.5" font-weight="700" fill="#0355a3" text-anchor="middle" font-family="Open Sans, sans-serif">Birchpoint</text>
    <g font-size="3.6" fill="#777" font-family="Open Sans, sans-serif">
      <text x="142" y="38" text-anchor="middle">Lorem ipsum dolor sit amet,</text><text x="142" y="43" text-anchor="middle">consectetur adipiscing elit</text>
      <text x="46" y="74">Lorem ipsum dolor sit amet,</text><text x="46" y="79">consectetur adipiscing elit</text>
      <text x="46" y="110">Lorem ipsum dolor sit amet,</text><text x="46" y="115">consectetur adipiscing elit</text>
      <text x="190" y="74">Lorem ipsum dolor sit amet,</text><text x="190" y="79">consectetur adipiscing elit</text>
      <text x="190" y="110">Lorem ipsum dolor sit amet,</text><text x="190" y="115">consectetur adipiscing elit</text>
      <text x="142" y="138" text-anchor="middle">Lorem ipsum dolor sit amet,</text><text x="142" y="143" text-anchor="middle">consectetur adipiscing elit</text>
    </g>
  </svg>
  <footer class="foot"><span class="line"></span><span class="mark">Birchpoint</span><span class="copy">Copyright © 2016 Birchpoint Consulting All rights reserved.</span><span class="num">18</span></footer>
</section>

<!-- 19 Content with icons -->
<section class="slide c1 r7">
  <div class="photo" style="inset:0;background:linear-gradient(90deg,#7d8a93,#a9b3b9 50%,#6f7b84)" role="img" aria-label="Photograph of doctors in discussion with a colleague"></div>
  <h2 class="overlay-title">Content With Icon Sample</h2>
  <div class="icons">
    <div class="icon-item"><div class="ic" style="background:var(--green)"><svg width="9" height="9" viewBox="0 0 10 10"><circle cx="4" cy="4" r="3" fill="none" stroke="#fff" stroke-width="1.3"/><line x1="6.2" y1="6.2" x2="9" y2="9" stroke="#fff" stroke-width="1.3"/></svg></div><b>Lorem Ipsum</b><p>Lorem ipsum dolor sit amet, consectetur adipiscing elit</p></div>
    <div class="icon-item"><div class="ic" style="background:var(--blue)"><svg width="9" height="9" viewBox="0 0 10 10"><rect x="1" y="1.5" width="8" height="5.5" fill="none" stroke="#fff" stroke-width="1.1"/><line x1="5" y1="7" x2="5" y2="9" stroke="#fff"/><line x1="3" y1="9" x2="7" y2="9" stroke="#fff"/></svg></div><b style="color:var(--blue)">Lorem Ipsum</b><p>Lorem ipsum dolor sit amet, consectetur adipiscing elit</p></div>
    <div class="icon-item"><div class="ic" style="background:var(--navy)"><svg width="9" height="9" viewBox="0 0 10 10"><circle cx="5" cy="5" r="2.2" fill="none" stroke="#fff" stroke-width="1.2"/><circle cx="5" cy="5" r="4" fill="none" stroke="#fff" stroke-width="1" stroke-dasharray="1.4 1"/></svg></div><b style="color:var(--navy)">Lorem Ipsum</b><p>Lorem ipsum dolor sit amet, consectetur adipiscing elit</p></div>
    <div class="icon-item"><div class="ic" style="background:var(--grey)"><svg width="9" height="9" viewBox="0 0 10 10"><line x1="2" y1="2" x2="8" y2="8" stroke="#fff" stroke-width="1.3"/><line x1="8" y1="2" x2="2" y2="8" stroke="#fff" stroke-width="1.3"/></svg></div><b style="color:#666">Lorem Ipsum</b><p>Lorem ipsum dolor sit amet, consectetur adipiscing elit</p></div>
  </div>
  <footer class="foot" style="background:#fff"><span class="line"></span><span class="mark">Birchpoint</span><span class="copy">Copyright © 2016 Birchpoint Consulting All rights reserved.</span><span class="num">19</span></footer>
</section>

<!-- 20 Testimonials -->
<section class="slide c2 r7">
  <div class="photo" style="inset:0;background:linear-gradient(90deg,#4f5559,#737a7e 50%,#555b5f)" role="img" aria-label="Darkened photograph of a doctor shaking hands with a patient"></div>
  <h2 class="overlay-title" style="left:0;right:0;text-align:center">Testimonials</h2>
  <svg style="position:absolute;left:130px;top:44px" width="26" height="26" viewBox="0 0 26 26"><circle cx="13" cy="13" r="11.5" fill="none" stroke="#abd036" stroke-width="1.5"/><text x="13" y="19" font-size="13" font-weight="700" fill="#abd036" text-anchor="middle" font-family="Open Sans, sans-serif">"</text></svg>
  <p style="position:absolute;left:22px;right:22px;top:84px;text-align:center;color:#fff;font-size:4.6px;line-height:6px">Lorem Ipsum is simply dummy text of the printing and typesetting industry. Lorem Ipsum has been the industry's standard dummy text ever since the 1500s, when an unknown printer took a galley of type and scrambled it to make a type specimen book.</p>
  <p style="position:absolute;left:0;right:0;top:110px;text-align:center;color:var(--green);font-size:4.6px;font-style:italic;font-weight:600">- John Doe -</p>
</section>

<!-- 21 Thank you -->
<section class="slide c3 r7 dark">
  <div class="photo" style="inset:0;background:linear-gradient(90deg,#1e1e1e,#2c2c2c 55%,#3a3f42)" role="img" aria-label="Darkened photograph of a medical team"></div>
  <svg class="photo" style="left:0;top:0" width="285" height="160" viewBox="0 0 285 160">
    <polygon points="0,8 120,8 140,22 285,22 285,25 138,25 118,11 0,11" fill="#1f9ad1"/>
    <polygon points="0,13 116,13 136,27 285,27 285,28.5 135,28.5 115,14.5 0,14.5" fill="#abd036"/>
    <polygon points="0,146 285,146 285,149 0,149" fill="#1f9ad1"/>
    <polygon points="0,150 285,150 285,151.5 0,151.5" fill="#abd036"/>
  </svg>
  <div style="position:absolute;left:10px;top:48px;color:#fff;font-size:9px;font-weight:600">THANK YOU FONT 24PT</div>
  <div style="position:absolute;left:10px;top:66px;color:#ddd;font-size:3.6px;line-height:4.6px">
    <b style="font-style:italic">ADDRESS</b><br>Lorem ipsum<br>
    <b style="font-style:italic">PHONE/FAX</b><br>Call: 555-010-0000<br>Lo-Call Number: 555-010-0006<br>
    <b style="font-style:italic">EMAIL</b><br>loremipsum@example.com<br>
    <b style="font-style:italic">WEBSITE</b><br>www.example.com
  </div>
  <div class="brand white" style="position:absolute;right:22px;top:40px">Birchpoint</div>
  <p style="position:absolute;left:162px;right:10px;top:102px;color:#ddd;font-size:3.8px;line-height:4.8px">Lorem Ipsum is simply dummy text of the printing and typesetting industry. Lorem Ipsum has been the industry's standard dummy text ever since the 1500s, when an unknown printer took a galley of type and scrambled it to make a type specimen. The industry's standard dummy text ever since the 1500s, when an unknown printer took a galley.</p>
</section>

</main>
</body>
</html>
```